Dental Business Card

I need Dental oriented business cards.
On the front side -
- on the first line, my name:
Dr Marlo Vintner
- on the second line (just underneath):
Doctor of Dental Medicine
- on the third line, or underneath that or in a corner, I would like the address and phone number:
5182 Ch. Birchfield
Montreal QC H2T 4B9
514-629-5074
- other than that i would maybe like a logo of a tooth, but i want it to be subtle and very basic!
- I would like the card to be preferably black or dark grey-ish with the writing in white
On the other side -
- 2-3 lines with the possibility to write the next appointment the box with the lines should be white, with the rest of the card being black

```html
<!DOCTYPE html>
<html lang="en">
<head>
<meta charset="utf-8">
<title>Dr Marlo Vintner — Business Card</title>
<link rel="stylesheet" href="https://fonts.googleapis.com/css2?family=Montserrat:wght@400;500;600&family=Open+Sans:wght@400&display=swap">
<style>
  :root {
    --backdrop: #2b2d30;
    --card-dark: #333538;
    --card-dark-edge: #26282a;
    --card-light: #ffffff;
    --ink-light: #ffffff;
    --ink-soft: #d4d6d9;
    --ink-dark: #2a2a2a;
    --rule-dark: #7c7f84;
    --rule-light: #c9c9c9;
  }
  * { margin: 0; padding: 0; box-sizing: border-box; }
  html, body {
    width: 1200px;
    height: 931px;
    overflow: hidden;
    background: var(--backdrop);
  }
  .stage {
    position: relative;
    width: 1200px;
    height: 931px;
  }
  .card {
    position: absolute;
    width: 520px;
    height: 297px;
    border-radius: 3px;
    box-shadow: 0 18px 40px rgba(0,0,0,0.45);
  }

  /* Front */
  .card-front {
    left: 60px;
    top: 430px;
    background: linear-gradient(135deg, #3a3c40 0%, var(--card-dark) 55%, var(--card-dark-edge) 100%);
    color: var(--ink-light);
    padding: 36px 40px;
  }
  .practice-mark {
    position: absolute;
    top: 30px;
    right: 44px;
    display: flex;
    align-items: center;
    gap: 8px;
    font-family: "Montserrat", sans-serif;
    font-weight: 500;
    font-size: 13px;
    letter-spacing: 2px;
    text-transform: uppercase;
    color: var(--ink-light);
  }
  .practice-mark .dot {
    width: 10px;
    height: 10px;
    border-radius: 50%;
    background: var(--ink-light);
  }
  .doctor-name {
    margin-top: 70px;
    font-family: "Montserrat", sans-serif;
    font-weight: 600;
    font-size: 33px;
    letter-spacing: 3px;
    text-transform: uppercase;
  }
  .doctor-title {
    margin-top: 4px;
    font-family: "Montserrat", sans-serif;
    font-weight: 400;
    font-size: 14px;
    letter-spacing: 3.2px;
    text-transform: uppercase;
    color: var(--ink-soft);
  }
  .front-rule {
    margin-top: 14px;
    height: 1px;
    background: var(--rule-dark);
  }
  .contact {
    margin-top: 14px;
    font-family: "Open Sans", sans-serif;
    font-size: 14px;
    line-height: 1.7;
    color: var(--ink-soft);
  }
  .contact .sep { margin: 0 8px; color: var(--rule-dark); }

  /* Back */
  .card-back {
    left: 620px;
    top: 150px;
    background: var(--card-light);
    color: var(--ink-dark);
    padding: 34px 40px;
  }
  .appointment-heading {
    text-align: right;
    font-family: "Montserrat", sans-serif;
    font-weight: 500;
    font-size: 19px;
    letter-spacing: 5px;
    text-transform: uppercase;
  }
  .write-lines {
    list-style: none;
    margin-top: 6px;
  }
  .write-lines li {
    height: 34px;
    border-bottom: 1px solid var(--rule-light);
  }
  .appointment-note {
    margin-top: 22px;
    font-family: "Open Sans", sans-serif;
    font-size: 11.5px;
    line-height: 1.5;
    color: #4a4a4a;
  }
</style>
</head>
<body>
  <main class="stage">
    <section class="card card-front" aria-label="Business card front">
      <div class="practice-mark"><span class="dot"></span>Vintner Dental</div>
      <h1 class="doctor-name">Dr Marlo Vintner</h1>
      <p class="doctor-title">Doctor of Dental Medicine</p>
      <div class="front-rule"></div>
      <p class="contact">
        5182 Ch. Birchfield<span class="sep">|</span>Montreal QC H2T 4B9<br>
        514 - 629 - 5074
      </p>
    </section>

    <section class="card card-back" aria-label="Appointment card back">
      <h2 class="appointment-heading">Appointment</h2>
      <ul class="write-lines">
        <li></li><li></li><li></li><li></li>
      </ul>
      <p class="appointment-note">
        If you are unable to keep your appointment,<br>
        please contact us as soon as possible.
      </p>
    </section>
  </main>
</body>
</html>
```